Business Card for Multi-Brand Sportswear Company

We are looking for a business card which represents our company and the multiple brands within it.

The company: Kelt Athletic (LTD)
The brands: Kelt, PawaLuni, VerdantFlex, Grit and Gale

Employees using these cards would be representing Kelt Athletic, rather than any of the individual brands. You will see a current design within the uploaded files, to give some inspiration. The actual text of the brands is not necessary, but the logos should be on there is some format.

Our creative minds on this are stretched, so we are looking for someone to make this their own, and show us what a good business card should look like.

We may like to get these printed with spot gloss, so keep that in mind with your designs.

www.keltathletic.co.uk

Industry/Entity Type

Business

Contact Information for Business Card

Tom Hollingsworth-Pryce
Operations Manager
(+44) 1632 960 418
Tom@keltathletic.co.uk
www.keltathletic.co.uk

Font styles to use
Sans Serif
Other font styles liked:
• Eurostile

Colors
ffffff

Requirements
Nice to have
• Dark (black) background

```html
<!DOCTYPE html>
<html lang="en">
<head>
<meta charset="utf-8">
<title>Kelt Athletic – Business Card</title>
<link rel="stylesheet" href="https://fonts.googleapis.com/css2?family=Open+Sans:ital,wght@0,400;0,700;1,400;1,700&display=swap">
<style>
  :root {
    --backdrop: #e3e3e5;
    --card: #222223;
    --red: #e8262d;
    --white: #ffffff;
    --mark-grey: #3c3c3e;
  }
  * { margin: 0; padding: 0; box-sizing: border-box; }
  html, body { width: 1200px; height: 1000px; overflow: hidden; }
  body {
    background: var(--backdrop);
    font-family: "Open Sans", Arial, sans-serif;
    position: relative;
  }
  .card {
    position: absolute;
    left: 266px;
    width: 666px;
    height: 397px;
    background: var(--card);
    overflow: hidden;
  }
  .card--front { top: 74px; }
  .card--back { top: 533px; }

  .brand-band { position: absolute; left: 0; top: 0; }
  .brand-name {
    position: absolute;
    left: 140px;
    top: 68px;
    width: 360px;
    text-align: center;
    color: var(--white);
    font-weight: 700;
    font-size: 30px;
    letter-spacing: 1px;
    text-transform: uppercase;
    line-height: 40px;
  }

  .holder { position: absolute; left: 118px; top: 186px; }
  .holder__name {
    color: var(--white);
    font-style: italic;
    font-weight: 700;
    font-size: 19px;
    letter-spacing: 0.3px;
    text-transform: uppercase;
  }
  .holder__role {
    color: var(--red);
    font-style: italic;
    font-size: 16px;
    margin-top: 2px;
  }

  .contacts { position: absolute; left: 110px; top: 263px; list-style: none; }
  .contacts li {
    display: flex;
    align-items: center;
    height: 28px;
    color: var(--white);
    font-style: italic;
    font-size: 17px;
  }
  .contacts svg { width: 29px; height: 18px; margin-right: 6px; flex: none; }

  .brand-marks {
    position: absolute;
    left: 420px;
    top: 298px;
    display: flex;
    gap: 20px;
    align-items: center;
  }
  .brand-marks svg { width: 32px; height: 24px; }

  .back-name {
    position: absolute;
    left: 0;
    top: 125px;
    width: 100%;
    text-align: center;
    color: var(--mark-grey);
    font-weight: 700;
    font-size: 100px;
    line-height: 120px;
    letter-spacing: 6px;
    text-transform: uppercase;
  }
</style>
</head>
<body>

<section class="card card--front" aria-label="Business card front">
  <svg class="brand-band" width="666" height="130" viewBox="0 0 666 130" aria-hidden="true">
    <polygon points="20,55 50,55 12,120 -18,120" fill="var(--red)"/>
    <polygon points="66,55 100,55 62,120 28,120" fill="var(--red)"/>
    <polygon points="117,55 522,55 460,120 79,120" fill="var(--red)"/>
  </svg>
  <div class="brand-name">Kelt Athletic</div>

  <div class="holder">
    <div class="holder__name">Tom Hollingsworth-Pryce</div>
    <div class="holder__role">Operations Manager</div>
  </div>

  <ul class="contacts">
    <li>
      <svg viewBox="0 0 29 18" aria-hidden="true">
        <polygon points="7,0 29,0 22,18 0,18" fill="var(--red)"/>
        <path d="M10 12 q0-5 5-5 q5 0 5 5 z" fill="var(--card)"/>
        <rect x="9" y="5" width="12" height="2" rx="1" fill="var(--card)"/>
      </svg>
      (+44) 1632 960 418
    </li>
    <li>
      <svg viewBox="0 0 29 18" aria-hidden="true">
        <polygon points="7,0 29,0 22,18 0,18" fill="var(--red)"/>
        <rect x="9" y="5" width="12" height="8" fill="none" stroke="var(--card)" stroke-width="1.5"/>
        <polyline points="9,5 15,10 21,5" fill="none" stroke="var(--card)" stroke-width="1.5"/>
      </svg>
      Tom@keltathletic.co.uk
    </li>
    <li>
      <svg viewBox="0 0 29 18" aria-hidden="true">
        <polygon points="7,0 29,0 22,18 0,18" fill="var(--red)"/>
        <circle cx="15" cy="9" r="5" fill="none" stroke="var(--card)" stroke-width="1.5"/>
        <line x1="10" y1="9" x2="20" y2="9" stroke="var(--card)" stroke-width="1.2"/>
        <line x1="15" y1="4" x2="15" y2="14" stroke="var(--card)" stroke-width="1.2"/>
      </svg>
      www.keltathletic.co.uk
    </li>
  </ul>

  <div class="brand-marks" aria-label="Group brands">
    <svg viewBox="0 0 32 24" role="img" aria-label="PawaLuni"><rect x="0" y="1" width="32" height="22" rx="2" fill="var(--red)"/></svg>
    <svg viewBox="0 0 32 24" role="img" aria-label="VerdantFlex"><rect x="4" y="2" width="22" height="20" rx="2" fill="none" stroke="var(--red)" stroke-width="2"/></svg>
    <svg viewBox="0 0 32 24" role="img" aria-label="Grit and Gale"><circle cx="14" cy="12" r="10" fill="none" stroke="var(--red)" stroke-width="2"/></svg>
  </div>
</section>

<section class="card card--back" aria-label="Business card back">
  <div class="back-name">Kelt</div>
</section>

</body>
</html>
```